JoltLane Merchant Discount Sticker

Project Overview:
JoltLane is an outdoor fitness brand offering discounts to members at select healthy food outlets. We require a sticker design for partner merchants to display, signaling to customers that exclusive deals are available for active GoCard holders (GoCard is the name for our class packages).

Design Purpose:
- Increase brand exposure
- Inform existing/potential customers about the benefits of JoltLane membership

Design Style:
- Minimal, clean, and bold
- Must include our logo
- Must include QR code to our trial page (website)
- Modern, eye-catching design that aligns with a fitness and wellness lifestyle

Brand Guidelines (see attachment). Fonts are whatever you think looks best with the brand. no preference beyond maybe 'Horizon'. We use Sora on the website.

Sticker Specifications:
Approximate size: 10 cm x 10 cm (square format). Adjust if you feel you have a better suggestion.

Single-sided design
Suitable to be stuck on glass windows.

Content to Include:
These are guidelines and you can adjust:
Ideas: "Show your GoCard to claim your discount", "Grab a discount here with JoltLane", "Grab a discount with your GoCard".
Sub, something like: "Grab a 7-day trial with JoltLane
Instagram handle with icon: @joltlanesg

Deliverables:
- Printable file format
- At least 1 round of revisions
~7 day turnaround time from project initiation

Additional Notes:
Please ensure the design is visually striking and easily read from a distance.

```html
<!DOCTYPE html>
<html lang="en">
<head>
<meta charset="utf-8">
<title>JoltLane Merchant Discount Sticker</title>
<link rel="stylesheet" href="https://fonts.googleapis.com/css2?family=Krona+One&family=Sora:wght@700&family=Open+Sans:wght@400&display=swap">
<style>
  :root {
    --ink: #3a3a3a;
    --mist: #d4d4d4;
    --sky: #8bbde6;
    --sky-deep: #6ec0ea;
    --paper: #ffffff;
  }
  html, body {
    margin: 0;
    padding: 0;
    width: 1200px;
    height: 1200px;
    overflow: hidden;
    background: var(--paper);
  }
  .sheet { display: block; width: 1200px; height: 1200px; }
  .headline { font-family: "Krona One", sans-serif; }
  .wordmark { font-family: "Krona One", sans-serif; }
  .tagline { font-family: "Open Sans", sans-serif; }
  .handle { font-family: "Sora", sans-serif; font-weight: 700; }
  .ink { fill: var(--ink); }
  .mist { fill: var(--mist); }
  .sky { fill: var(--sky); }
  .outline-text { fill: none; stroke: var(--sky); stroke-width: 2; }
  .hole { fill: var(--paper); }
</style>
</head>
<body>
<svg class="sheet" viewBox="0 0 1920 1920" xmlns="http://www.w3.org/2000/svg">
  <defs>
    <path id="bell-outline" d="M274,980 V815 A126,126 0 0 1 400,689 H717 A126,126 0 0 1 843,815 V980 A393,393 0 0 1 730,1603 Q558,1632 385,1603 A393,393 0 0 1 274,980 Z"/>
    <path id="bell-hole" d="M354,890 V815 Q354,769 400,769 H717 Q763,769 763,815 V890 Q763,910 735,900 Q558,810 382,900 Q354,910 354,890 Z"/>
    <linearGradient id="light-fill" gradientUnits="userSpaceOnUse" x1="0" y1="689" x2="0" y2="1620">
      <stop offset="0" stop-color="#d4d4d4"/>
      <stop offset="0.45" stop-color="#d1d3d5"/>
      <stop offset="1" stop-color="#6ec0ea"/>
    </linearGradient>
    <linearGradient id="dark-fill" gradientUnits="userSpaceOnUse" x1="0" y1="689" x2="0" y2="1620">
      <stop offset="0" stop-color="#3a3a3a"/>
      <stop offset="0.5" stop-color="#3d4043"/>
      <stop offset="1" stop-color="#6ab4dd"/>
    </linearGradient>
    <linearGradient id="band-fade" x1="0" y1="0" x2="0" y2="1">
      <stop offset="0" stop-color="#7aa3bf"/>
      <stop offset="0.6" stop-color="#d4d4d4"/>
    </linearGradient>
    <path id="arc-light" d="M240,1310 A321,321 0 1 1 876,1310"/>
    <path id="arc-dark-top" d="M1045,880 A330,330 0 0 1 1705,880"/>
    <path id="arc-dark-trial" d="M1118,1105 Q1375,1030 1632,1100"/>
  </defs>

  <!-- Light sticker -->
  <g class="sticker sticker--light">
    <use href="#bell-outline" fill="url(#light-fill)"/>
    <use href="#bell-hole" class="hole"/>
    <text class="headline ink" font-size="38">
      <textPath href="#arc-light" startOffset="50%" text-anchor="middle">GRAB A DISCOUNT WITH YOUR GOCARD</textPath>
    </text>
    <text class="wordmark ink" x="558" y="1160" font-size="64" text-anchor="middle">JoltLane</text>
    <text class="tagline ink" x="558" y="1318" font-size="20" text-anchor="middle">we move you</text>
    <text class="headline ink" x="558" y="1392" font-size="34" text-anchor="middle">START A 7-DAY TRIAL</text>
    <text class="headline ink" x="558" y="1430" font-size="34" text-anchor="middle">WITH JOLTLANE</text>
    <path class="ink" d="M298,1502 Q558,1418 818,1502 Q740,1575 558,1577 Q376,1575 298,1502 Z"/>
    <rect x="451" y="1505" width="27" height="27" rx="7" fill="none" stroke="var(--sky)" stroke-width="3"/>
    <text class="handle sky" x="494" y="1530" font-size="30">@joltlanesg</text>
  </g>

  <!-- Dark sticker -->
  <g class="sticker sticker--dark">
    <use href="#bell-outline" transform="translate(817,-370)" fill="url(#dark-fill)"/>
    <use href="#bell-hole" transform="translate(817,-370)" class="hole"/>
    <text class="headline sky" font-size="70" letter-spacing="2">
      <textPath href="#arc-dark-top" startOffset="50%" text-anchor="middle">GRAB A DISCOUNT</textPath>
    </text>
    <text class="headline outline-text" x="1375" y="678" font-size="32" text-anchor="middle">WITH YOUR</text>
    <text class="headline outline-text" x="1375" y="716" font-size="32" text-anchor="middle">GOCARD</text>
    <text class="wordmark mist" x="1375" y="885" font-size="60" text-anchor="middle">JoltLane</text>
    <text class="tagline mist" x="1375" y="1018" font-size="16" text-anchor="middle">we move you</text>
    <text class="headline" fill="#a9cdea" font-size="19">
      <textPath href="#arc-dark-trial" startOffset="50%" text-anchor="middle">START A 7-DAY TRIAL WITH JOLTLANE</textPath>
    </text>
    <path fill="url(#band-fade)" d="M1115,1128 Q1375,1060 1635,1128 Q1550,1200 1375,1200 Q1200,1200 1115,1128 Z"/>
    <rect x="1267" y="1130" width="27" height="27" rx="7" fill="none" stroke="var(--ink)" stroke-width="3"/>
    <text class="handle ink" x="1310" y="1155" font-size="30">@joltlanesg</text>
  </g>
</svg>
</body>
</html>
```